VerdaTurfix - 11" x 4" Door Hanger, full color both sides

We need a door hanger designed, 11" x 4", full color both sides, We are a lawn care company that provides lawn mowing, and other services to clients. This door hanger will be place on the 9 neighbors of our current clients. The ad needs to state that we provided lawn service to one of their neighbors today, and that we are in their neighborhood each week on that day. The door hanger will have 4 printings, substituting the day of Tuesday, Wednesday, Thursday, and Friday. All the art work and text will remain the same except the day of the week. For information about VerdaTurfix, please visit our website www.verdaturfix.net. The main emphasis of the message should be that we are their every week on that day, and the benefits to them of using our service (ie. quality time with their family, golf, sports, resting, etc., instead of mowing the lawn). At the bottom of the door hanger will be a coupon offering their tenth (10th) lawn service free, which is the same as a 10% discount.

I have uploaded a template files for the front and back of an 11 x 4 door hanger, The templates are pdf, jpeg, or eps files. The final product can be a pdf, jpeg, or eps file.

Target Market(s)

Neighbors of our existing clients

Industry/Entity Type

Lawn Care

Font styles to use
Serif

Requirements
Must have
• Professional design and art, Short conversational message that relays the following thoughts:
• 1. We mowed your neighbor's lawn today!
• 2. We are in your neighborhood every Tuesday!
• 3. Our lawn service is guaranteed.
• 4. Call to action - Call us today! 555-014-7382
• 5. Of course our contact info, name, phone number, website address.
• 6. Coupon at bottom for "10th lawn service Free!"
Nice to have
• Art work from our website is fine to use, That carries our theme throughout our campaign.
Should not have
• Very wordy. This is basically a billboard, Have very few seconds to grab their attention.

```html
<!DOCTYPE html>
<html lang="en">
<head>
<meta charset="utf-8">
<title>VerdaTurfix Door Hanger</title>
<link rel="stylesheet" href="https://fonts.googleapis.com/css2?family=Anton&family=Archivo+Black&family=Permanent+Marker&family=Open+Sans:wght@400;700;800&display=swap">
<style>
  :root {
    --white: #ffffff;
    --black: #000000;
    --ink: #111111;
    --lime: #8fdc1e;
    --lime-light: #b6ef3a;
    --grass-dark: #3f7d0c;
    --grass-mid: #7cc11a;
    --grass-glow: #e4f27a;
    --banner-green: #a6e53a;
    --red: #e2231a;
    --mower-red: #c8211c;
  }
  * { margin: 0; padding: 0; box-sizing: border-box; }
  html, body { width: 951px; height: 1200px; overflow: hidden; background: var(--white); }
  body { position: relative; font-family: "Open Sans", Arial, sans-serif; }

  .hanger { position: absolute; top: 0; width: 453px; height: 1200px; overflow: hidden; background: var(--white); }
  .hanger--front { left: 0; }
  .hanger--back { left: 498px; }

  .day-header { position: absolute; top: 0; left: 0; width: 100%; height: 107px; text-align: center; }
  .day-header__intro { position: absolute; top: 40px; width: 100%; font-size: 18px; color: var(--ink); }
  .day-header__day { position: absolute; top: 62px; width: 100%; font-family: "Archivo Black", Arial, sans-serif; font-size: 42px; letter-spacing: 2px; transform: scaleX(1.25); color: var(--black); line-height: 1; }

  .contact-band { position: absolute; left: 0; top: 1014px; width: 100%; height: 186px; background: var(--black); color: var(--white); text-align: center; }
  .contact-band__name { position: absolute; top: 22px; width: 100%; font-size: 42px; letter-spacing: 1px; line-height: 1; }
  .contact-band__call { position: absolute; top: 72px; width: 100%; font-size: 27px; line-height: 1; }
  .contact-band__call strong { font-weight: 800; }
  .contact-band__web { position: absolute; top: 106px; width: 100%; font-family: "Anton", Impact, sans-serif; font-size: 40px; letter-spacing: 1px; line-height: 1.2; }

  /* Front */
  .front-field { position: absolute; left: 0; top: 107px; width: 453px; height: 907px;
    background: radial-gradient(ellipse at 55% 25%, var(--grass-glow) 0%, var(--lime-light) 30%, var(--grass-mid) 65%, var(--grass-dark) 100%); }
  .outlined { color: var(--white); text-shadow: -3px -3px 0 var(--black), 3px -3px 0 var(--black), -3px 3px 0 var(--black), 3px 3px 0 var(--black), 0 4px 0 var(--black), 4px 0 0 var(--black), 0 -4px 0 var(--black), -4px 0 0 var(--black), 6px 6px 8px rgba(0,0,0,.45); }
  .offer__get { position: absolute; left: 40px; top: 200px; font-family: "Permanent Marker", cursive; font-size: 40px; line-height: .95; transform: rotate(-10deg); }
  .offer__tenth { position: absolute; left: 0; top: 285px; width: 100%; text-align: center; font-family: "Anton", Impact, sans-serif; font-size: 132px; line-height: 1; padding-left: 40px; }
  .offer__lawn { position: absolute; left: 0; top: 415px; width: 100%; text-align: center; font-family: "Anton", Impact, sans-serif; font-size: 104px; line-height: 1; padding-left: 40px; }
  .offer__service { position: absolute; left: 0; top: 512px; width: 100%; text-align: center; font-family: "Anton", Impact, sans-serif; font-size: 76px; line-height: 1; padding-left: 40px; letter-spacing: 1px; }
  .offer__free { position: absolute; left: 20px; top: 580px; font-family: "Permanent Marker", cursive; font-size: 128px; line-height: 1; transform: rotate(-7deg); }
  .offer__details { position: absolute; left: 218px; top: 728px; width: 225px; text-align: center; font-size: 15.5px; font-weight: 700; line-height: 1.2; color: var(--black); }
  .photo-mower { position: absolute; left: 28px; top: 712px; width: 196px; height: 168px; border-radius: 20px 40px 10px 10px;
    background: linear-gradient(160deg, var(--mower-red) 0%, #7a1210 60%, #222 100%); }
  .photo-tablet { position: absolute; left: 228px; top: 836px; width: 225px; height: 178px; border-radius: 14px 0 0 0;
    background: linear-gradient(135deg, #2a2a2a 0%, #4f8f22 45%, #d8b49a 100%); }
  .experience-badge { position: absolute; left: 51px; top: 864px; width: 120px; height: 120px; border-radius: 50%; background: var(--black); border: 4px solid var(--white); }

  /* Back */
  .back-field { position: absolute; left: 0; top: 107px; width: 453px; height: 907px;
    background: radial-gradient(ellipse at 50% 15%, var(--lime-light) 0%, var(--lime) 55%, #6fc613 100%); }
  .back-field__swoosh { position: absolute; left: 0; top: 740px; width: 453px; height: 274px; }
  .headline { position: absolute; left: 0; top: 272px; width: 100%; text-align: center; font-family: "Anton", Impact, sans-serif; font-size: 56px; line-height: 1.02; letter-spacing: .5px; }
  .mission { position: absolute; left: 2px; top: 460px; width: 184px; text-align: right; color: var(--white); font-size: 15px; font-weight: 800; line-height: 1.2; }
  .services { position: absolute; left: 196px; top: 459px; width: 257px; color: var(--ink); font-size: 14px; line-height: 1.22; }
  .services h3 { font-size: 14px; font-weight: 800; }
  .services ul { list-style: none; }
  .services li { padding-left: 12px; text-indent: -12px; }
  .services li::before { content: "\2022\00a0"; }
  .coupon { position: absolute; left: 40px; top: 843px; width: 373px; height: 94px; background: var(--banner-green); border: 2px solid var(--white); box-shadow: 0 2px 4px rgba(0,0,0,.3); }
  .coupon__icon { position: absolute; left: 14px; top: 14px; width: 68px; height: 62px; }
  .coupon__free { position: absolute; left: 92px; top: 12px; font-family: "Anton", Impact, sans-serif; font-size: 60px; color: var(--red); line-height: 1; transform: rotate(-4deg); font-style: normal; }
  .coupon__label { position: absolute; left: 225px; top: 10px; font-family: "Anton", Impact, sans-serif; font-size: 36px; line-height: 1.05; color: var(--black); text-align: left; }
  .coupon__terms { position: absolute; left: 0; top: 944px; width: 100%; text-align: center; font-size: 13.5px; line-height: 1.3; color: var(--ink); }
</style>
</head>
<body>

<section class="hanger hanger--front">
  <header class="day-header">
    <p class="day-header__intro">We are in your neighborhood every</p>
    <p class="day-header__day">TUESDAY</p>
  </header>

  <div class="front-field" role="img" aria-label="Sunlit close-up of green grass blades"></div>

  <p class="offer__get outlined">GET<br>YOUR</p>
  <p class="offer__tenth outlined">10th</p>
  <p class="offer__lawn outlined">LAWN</p>
  <p class="offer__service outlined">SERVICE</p>
  <p class="offer__free outlined">FREE!</p>

  <div class="photo-mower" role="img" aria-label="Red ride-on lawn mower"></div>
  <p class="offer__details">Call today for details of this special offer or go online to discover more about our guaranteed lawn service.</p>
  <div class="photo-tablet" role="img" aria-label="Hand tapping a tablet showing the lawn care website"></div>
  <div class="experience-badge" aria-label="Experience badge"></div>

  <footer class="contact-band">
    <p class="contact-band__name">VERDATURFIX</p>
    <p class="contact-band__call">Call us today! <strong>555-014-7382</strong></p>
    <p class="contact-band__web">www.verdaturfix.net</p>
  </footer>
</section>

<section class="hanger hanger--back">
  <header class="day-header">
    <p class="day-header__intro">We are in your neighborhood every</p>
    <p class="day-header__day">TUESDAY</p>
  </header>

  <div class="back-field">
    <svg class="back-field__swoosh" viewBox="0 0 453 274" preserveAspectRatio="none">
      <path d="M0 40 Q230 70 453 0 L453 274 L0 274 Z" fill="#ffffff"/>
      <path d="M0 30 Q230 62 453 -8 L453 0 Q230 70 0 40 Z" fill="#d9f59a"/>
    </svg>
  </div>

  <h1 class="headline outlined">We mowed<br>your neighbor's<br>lawn today!</h1>

  <p class="mission">VerdaTurfix is a family owned company with a mission to bring service excellence to our client throughout our whole operation. By providing our clients guaranteed service excellence, they are able to spend quality time with their family, rather than doing lawn work.</p>

  <div class="services">
    <h3>VerdaTurfix provides the following services:</h3>
    <ul>
      <li>Weekly and bi-weekly lawn care service</li>
      <li>Fertilization and weed control services</li>
      <li>Lawn insect, grub worm and fire ant control</li>
      <li>Sprinkler repair, and irrigation modification</li>
    </ul>
    <h3>Other landscape services, including but not limited to:</h3>
    <ul>
      <li>Planting plants and trees</li>
      <li>Seasonal flowers</li>
      <li>Trimming of plants and hedges</li>
      <li>Providing and installing mulch</li>
      <li>Providing and installing stone or metal planting bed borders</li>
      <li>Additional services.</li>
    </ul>
  </div>

  <div class="coupon">
    <svg class="coupon__icon" viewBox="0 0 68 62" aria-label="Push mower icon">
      <path d="M2 2 L22 30" stroke="#000" stroke-width="4" stroke-linecap="round"/>
      <path d="M14 28 H60 L64 46 H10 Z" fill="#000"/>
      <circle cx="18" cy="52" r="8" fill="#000"/>
      <circle cx="56" cy="52" r="8" fill="#000"/>
    </svg>
    <span class="coupon__free">FREE</span>
    <span class="coupon__label">MOWING<br>SERVICE</span>
  </div>
  <p class="coupon__terms">Use this door hanger to get your tenth lawn mowing<br>session free when block booking. Call for full details.</p>

  <footer class="contact-band">
    <p class="contact-band__name">VERDATURFIX</p>
    <p class="contact-band__call">Call us today! <strong>555-014-7382</strong></p>
    <p class="contact-band__web">www.verdaturfix.net</p>
  </footer>
</section>

</body>
</html>
```